Social Business Consultancy

Kavora Ventures is a start up consultancy but with a difference: were non-corporate. We work in the field of economic development in low income countries and we focus on entrepreneurship but with a social and or environmental mission.

The type of projects we work on are innovative, ground breaking, different, edgy and bold. We are young, determined, , unreasonnable and undeterred by challenges.
We want our website to convey these ideas.
Updates

Hello,

Could you please include the option of having the website in two languages. Thank you.

Please note that new files have been added to the project brief.

- FrontPage  Main Photo (Grey dirt Road)
- WordCloud Photo to be used on the home page (as a small image )

The website should keep these colour tones.

Thank you !

Hello,

Wireframes have been uploaded. Please use as an indication.

Thanks,
n.

Target Market(s)

Governments, development agencies, social investors, NGOs, banks and social entrepreneurs.

Industry/Entity Type

Consulting

Requirements
Must have
• We already have a logo and business cards (provided). We want the website to look professional, yet simple with a maximum of two or three colours. We want the look to be seamless. There is no need for too many boxes or categories.
Nice to have
• We want bold, edgy, modern  and professional look .
• Examples:
• http://www.brightmarrowlab.org/
• http://www.pavelstone.com/
• http://www.tarnhiring.co.nz/
Should not have
• The design should not use old style fonts.

```html
<!DOCTYPE html>
<html lang="en">
<head>
<meta charset="utf-8">
<title>Kavora Ventures — Social Business Consultancy</title>
<link rel="stylesheet" href="https://fonts.googleapis.com/css2?family=Arimo:wght@400&family=Cinzel:wght@400&display=swap">
<style>
:root{
  --lime:#b8c52c;
  --lime-deep:#a6b51f;
  --lime-text:#a7b51c;
  --ink:#1e1e12;
  --grey-dark:#5f6062;
  --grey-text:#6a6a6a;
  --body-text:#3a3a3a;
  --rule:#e4e4e4;
  --white:#ffffff;
  --blue-top:#55c9f0;
  --blue-bottom:#1fa3dc;
}
*{margin:0;padding:0;box-sizing:border-box}
html,body{width:1200px;height:858px;overflow:hidden;background:var(--white)}
body{font-family:'Arimo',Arial,sans-serif;position:relative}

.site-header{position:absolute;left:0;top:0;width:1200px;height:117px;
  background:linear-gradient(#ffffff,#f4f4f4)}
.brand{position:absolute;left:184px;top:30px;display:flex;align-items:center;gap:10px}
.brand-name{font-size:30px;color:var(--grey-dark);letter-spacing:.5px}
.brand-mark{width:34px;height:34px;background:var(--lime)}

.main-nav{position:absolute;left:663px;top:40px;width:361px;height:35px;
  background:var(--grey-dark);border-radius:6px;display:flex;align-items:center;padding-left:13px}
.main-nav a{color:var(--white);text-decoration:none;font-size:14px;height:35px;line-height:35px;padding:0 9px}
.main-nav a.is-active{background:var(--lime);color:#111}

.hero{position:absolute;left:0;top:117px;width:1200px;height:328px;background:var(--lime);overflow:hidden}
.hero-photo{position:absolute;right:0;top:0;width:670px;height:328px;
  background:radial-gradient(ellipse at 70% 40%,#d9d39a 0%,#c4c35a 30%,rgba(184,197,44,0) 70%),
  linear-gradient(90deg,rgba(184,197,44,1) 0%,rgba(190,198,80,.6) 40%,rgba(200,196,120,.7) 100%)}
.hero-title{position:absolute;left:179px;top:30px;font-family:'Cinzel',Georgia,serif;color:var(--ink);
  font-size:41px;line-height:53px;font-weight:400}
.hero-title span{display:block}
.hero-title span+span{padding-left:127px}
.hero-text{position:absolute;left:179px;top:266px;top:149px;width:337px;font-size:12.5px;line-height:21.2px;
  color:#4d5416;letter-spacing:.2px}
.btn-more{position:absolute;left:179px;top:251px;width:169px;height:36px;border-radius:9px;
  background:linear-gradient(var(--blue-top),var(--blue-bottom));border:1px solid #1b8fc4;
  color:var(--white);font-size:17px;line-height:34px;padding-left:17px;text-decoration:none}

.content{position:absolute;left:0;top:445px;width:1200px;height:330px;
  background:linear-gradient(#ececec 0,#ffffff 40px,#ffffff 275px,#dedede 330px)}
.col{position:absolute;top:48px;width:265px}
.col-welcome{left:177px}
.col-what{left:468px}
.col-posts{left:759px}
.col h2{font-weight:400;font-size:23px;color:var(--grey-text);padding:0 0 0 2px;height:31px;border-bottom:1px solid var(--rule)}
.col h2 em{font-style:normal;color:var(--lime-text)}
.col p{font-size:11.3px;line-height:21.2px;color:var(--body-text);text-align:justify;letter-spacing:.35px;padding-left:2px;margin-top:12px}
.col p+p{margin-top:21px}
.col-what p{margin-top:10px}
.wordcloud{display:block;margin:16px 0 0 7px;width:249px;height:65px;
  background:linear-gradient(90deg,#b6c22c,#c9cf6a 50%,#b6c22c);box-shadow:0 1px 3px rgba(0,0,0,.25)}
.post-list{list-style:none;margin-top:12px}
.post-list li{font-size:11.3px;color:var(--body-text);letter-spacing:.35px;height:31px;line-height:22px;padding-left:3px}
.post-list li::before{content:"»";margin-right:4px}

.site-footer{position:absolute;left:0;top:775px;width:1200px;height:83px;background:var(--grey-dark);
  border-top:1px solid #8c8c8c;color:var(--white);font-size:11.5px;text-align:center;line-height:82px;letter-spacing:.2px}
</style>
</head>
<body>
<header class="site-header">
  <div class="brand"><span class="brand-name">Kavora Ventures</span><span class="brand-mark"></span></div>
  <nav class="main-nav">
    <a class="is-active" href="#">Home</a><a href="#">Blog</a><a href="#">About Us</a><a href="#">Services</a><a href="#">Contact Us</a>
  </nav>
</header>

<section class="hero">
  <div class="hero-photo" role="img" aria-label="Photo of a man sketching a database diagram on glass with a marker, tinted lime"></div>
  <h1 class="hero-title"><span>BE PART OF</span><span>THE CHANGE</span></h1>
  <p class="hero-text">Lorem Ipsum has been the industry's standard dummy text ever since the 1500s, when an unknown printer took a galley of type and scrambled it to make a type specimen book. It has survived not only five centuries.</p>
  <a class="btn-more" href="#">Read More Info...</a>
</section>

<main class="content">
  <section class="col col-welcome">
    <h2>Welcome To <em>KAVORA</em></h2>
    <p>Contrary to popular belief, Lorem Ipsum is not simply random text. It has roots in a piece of classical Latin literature from 45 BC.</p>
    <p>Making it over 2000 years old. Tomas Reddale, a Latin professor at Ashford-Lyle College in Virginia, looked up one of the more obscure Latin words, consectetur.</p>
  </section>
  <section class="col col-what">
    <h2>What We <em>DO?</em></h2>
    <div class="wordcloud" role="img" aria-label="Lime word cloud of social business themes"></div>
    <p>Making it over 2000 years old. Tomas Reddale, a Latin professor at Ashford-Lyle College in Virginia, looked up one of the more obscure Latin words, consectetur.</p>
  </section>
  <section class="col col-posts">
    <h2>Recent &nbsp;<em>POST !</em></h2>
    <ul class="post-list">
      <li>It's not always about the money</li>
      <li>The journey begins here</li>
      <li>A word from my good lady wife</li>
      <li>It's not always about the money</li>
      <li>The journey begins here</li>
      <li>A word from my good lady wife</li>
    </ul>
  </section>
</main>

<footer class="site-footer">© 2010 Kavora Ventures.&nbsp; All Rights Reserved.</footer>
</body>
</html>
```